MAKE KLV WEBSITE GREAT AGAIN :)

KLV is a successful travel company organizing incentives, conferences, VIP and group travel for high-end clients.
For our existing website - www.klvrota.com - in Divi theme we need an attractive design reflecting the beauty of our country Turkey and the professional. reliable services given by our company. The content (texts etc) have recently been done by one of our staff members but the site clearly lacks design and the professional touch to retain visitors' attention. At the moment, our home page is totally white and the text is written in unattractive fonts and colours.

Note 1: The content has been written already mostly focusing on keywords and SEO.
The pages are existing already except that we need to move the testimonials from KLV TEAM to a separate TESTIMONIAL page and one page called DESTINO TURQUIA must be added

Pages should be as follows
* HOME
* WHAT WE DO BEST
* TURKEY DESTINATIONS
-- Istanbul
-- Cappadocia
-- Antalya
-- Izmir
-- Bodrum
-- North Cyprus
* KLV TEAM
* TESTIMONIALS (must be added as it is not on the present site)
* DESTINO TURQUIA (not in the present site)
* CONTACT US

NOTE 2. CODING
* Besides the existing links we need a link to our Blog (www.mywanderbasket.com)
* and a banner with the latest Facebook posts

NOTE 3. The DESIGN should be a nice mix of modern style and oriental flair
Turkey is a colourful country and has a wealth of historical and cultural places. This should be reflected through the power of photos (which we fell it does not with the present design)

NOTE 4: We need to resize some photos and will submit alter

WORLDWIDE

Tourism

5+ page

• a nice modern airy font

• When visiting our site, it should be instantaneously clear that we sell travel programs to TURKEY.
• Nice mix of elegant, modern design paired with Ottoman touches.
• Our company logo features an Ottoman tulip which could be used to mark titles or instead of bullets for instance
• Ref. company logo: next to the actual image logo - should be written
• Kestrel Lumen Voyages
• Possibly the colours featured in our logo could also be used in the web design - if not, then of course colours which will not clash with the logo.
• Ref logo - we would like to have it feature in a good size - not too small (like now) not too large to be overpowering, yet the visitor should clearly see teh company identity
• old fashioned look
• Turkey/Istanbul is a modern place with brilliant infrastructure, this should be reflected in teh site

```html
<!DOCTYPE html>
<html lang="en">
<head>
<meta charset="utf-8">
<title>KLV – Kestrel Lumen Voyages</title>
<link href="https://fonts.googleapis.com/css2?family=Open+Sans:wght@400;600;700&family=Roboto:wght@400;500;700&display=swap" rel="stylesheet">
<style>
:root{
  --purple:#5e1b63;
  --purple-dark:#3f1043;
  --teal:#2a8db3;
  --teal-dark:#1f6f8f;
  --ink:#2b2b2b;
  --muted:#6d6d6d;
  --line:#e3e3e3;
  --footer:#eeeeee;
}
*{box-sizing:border-box;margin:0;padding:0}
html,body{width:1200px;height:3681px;overflow:hidden}
body{font-family:"Open Sans",Arial,sans-serif;color:var(--ink);background:#fff;position:relative}
.abs{position:absolute}
h2{font-family:"Roboto",Arial,sans-serif}

/* header */
.site-header{left:0;top:0;width:1200px;height:105px;background:#fff;z-index:3;box-shadow:0 1px 4px rgba(0,0,0,.15)}
.topbar{right:98px;top:26px;display:flex;gap:38px;font-size:14px;color:#555}
.topbar span{display:flex;align-items:center;gap:12px}
.topbar i{display:inline-block;width:22px;height:22px;background:#eee;border-radius:3px;position:relative}
.topbar svg{position:absolute;left:4px;top:4px}
.main-nav{right:98px;top:68px;display:flex;gap:26px;font-family:"Roboto",sans-serif;font-size:14px;font-weight:500;color:var(--ink)}
.main-nav .active{color:var(--purple)}
.brand{left:145px;top:14px;width:88px;height:128px;background:var(--purple);z-index:4;display:flex;align-items:center;justify-content:center;color:#fff;font-family:"Roboto",sans-serif;font-weight:700;font-size:30px}
.brand-line{left:100px;top:138px;font-size:13px;color:#fff;z-index:4;font-weight:600}

/* hero */
.hero{left:0;top:105px;width:1200px;height:452px;background:radial-gradient(circle at 40% 60%,#2f6fb8 0,#1f4f8c 30%,#6b7b66 62%,#9fa49a 100%)}
.hero-title{left:0;width:1200px;top:245px;text-align:center;color:#fff;font-family:"Roboto",sans-serif;font-weight:700;font-size:37px;line-height:48px;text-shadow:0 2px 4px rgba(0,0,0,.35)}
.btn{background:var(--teal);color:#fff;font-family:"Roboto",sans-serif;font-weight:700;font-size:13px;text-align:center;border-radius:3px;box-shadow:0 3px 0 var(--teal-dark)}
.hero-btn{left:520px;top:372px;width:160px;height:34px;line-height:34px}
.arrow-btn{width:40px;height:40px;border:2px solid #fff;border-radius:4px;display:flex;align-items:center;justify-content:center}

/* section heading */
.sec-title{left:0;width:1200px;text-align:center;font-size:28px;font-weight:700;color:#222;display:flex;justify-content:center;align-items:center;gap:12px}
.sec-title .mark{width:18px;height:18px;border-radius:50%;background:var(--purple)}

.intro{left:200px;width:800px;top:670px;text-align:center;font-size:13px;line-height:22px;color:#666}
.services{left:65px;top:808px;width:1070px;display:flex;justify-content:space-between}
.service{width:150px;text-align:center;font-family:"Roboto",sans-serif;font-size:15px;font-weight:500;color:#333;line-height:20px}
.service svg{display:block;margin:0 auto 22px}

/* destinations */
.dest-panel{left:0;top:1006px;width:650px;height:530px;background:linear-gradient(135deg,#4a4643,#2f2d2b)}
.dest-photo{left:572px;top:1055px;width:628px;height:432px;background:linear-gradient(180deg,#2f64b0 0%,#4c8fd6 55%,#2d4e7a 100%)}
.dest-title{left:80px;top:1070px;color:#fff;font-size:28px;font-weight:700;display:flex;gap:12px;align-items:center}
.dest-title .mark{width:18px;height:18px;border-radius:50%;background:#fff}
.dest-text{left:98px;top:1130px;width:400px;color:#fff;font-size:15px;line-height:24px;font-weight:600}
.dest-list{left:98px;top:1228px;list-style:none;color:#fff;font-family:"Roboto",sans-serif;font-size:14px;font-weight:700}
.dest-list li{height:35px;display:flex;align-items:center;gap:10px}
.dest-list li::before{content:"";width:12px;height:12px;border:2px solid #fff;border-radius:50%}
.dest-list li.on::before{background:var(--teal);border-color:var(--teal)}
.dest-btn{left:98px;top:1446px;width:160px;height:36px;line-height:36px}
.small-arrows{left:1038px;top:1098px;display:flex;gap:10px}
.small-arrows span{width:26px;height:26px;border:2px solid #fff;border-radius:4px;display:flex;align-items:center;justify-content:center}

/* cards */
.card{width:490px;height:294px;border:4px solid #fff;box-shadow:0 1px 4px rgba(0,0,0,.3);overflow:hidden}
.card-photo{position:absolute;inset:0}
.card-shade{position:absolute;left:0;right:0;bottom:0;height:110px;background:linear-gradient(180deg,rgba(0,0,0,0),rgba(0,0,0,.8))}
.card h3{position:absolute;left:14px;bottom:46px;color:#fff;font-family:"Roboto",sans-serif;font-size:20px;font-weight:500}
.card p{position:absolute;left:14px;bottom:10px;width:360px;color:#eee;font-size:11px;line-height:15px}
.card .stars{position:absolute;right:12px;bottom:10px;color:#e6b422;font-size:13px;letter-spacing:1px}
.view-btn{left:520px;top:2328px;width:160px;height:36px;line-height:36px}

/* join */
.join{left:0;top:2442px;width:1200px;height:373px;background:linear-gradient(90deg,#2e1d1b,#4a2a24 60%,#2d1b18)}
.join-photo{left:690px;top:2442px;width:510px;height:373px;background:linear-gradient(90deg,rgba(74,42,36,0),#5a3a33 35%,#6e4c43 70%,#4a2e28)}
.join-title{left:80px;top:2500px;color:#fff;font-size:28px;font-weight:700;display:flex;gap:12px;align-items:center}
.join-title .mark{width:18px;height:18px;border-radius:50%;background:#fff}
.join-text{left:98px;top:2548px;width:560px;color:#fff;font-size:20px;line-height:30px;font-weight:600}
.join-input{left:98px;top:2640px;width:432px;height:50px;border:2px solid #ddd;color:#ccc;font-size:12px;padding:15px 18px}
.join-btn{left:98px;top:2719px;width:160px;height:36px;line-height:36px}

/* blog */
.post{width:304px;height:317px;background:#fff;box-shadow:0 1px 5px rgba(0,0,0,.2)}
.post-photo{position:absolute;left:0;top:0;width:304px;height:147px}
.post-date{position:absolute;left:14px;top:117px;width:54px;height:62px;background:var(--purple);color:#fff;text-align:center;font-family:"Roboto",sans-serif;font-size:13px;font-weight:700;padding-top:12px;line-height:18px}
.post-meta{position:absolute;left:14px;top:188px;font-size:12px;color:#444;display:flex;gap:12px}
.post-meta span{display:flex;align-items:center;gap:4px}
.post h4{position:absolute;left:14px;top:212px;font-family:"Roboto",sans-serif;font-size:15px;font-weight:500}
.post p{position:absolute;left:14px;top:236px;width:270px;font-size:12px;line-height:17px;color:#555}
.post .more{position:absolute;left:14px;top:282px;font-size:12px;font-weight:700;color:var(--teal)}
.side-arrow{width:38px;height:38px;border:2px solid #bbb;border-radius:4px;display:flex;align-items:center;justify-content:center;background:#fff}

/* footer */
.site-footer{left:0;top:3328px;width:1200px;height:304px;background:var(--footer)}
.foot-h{font-family:"Roboto",sans-serif;font-size:14px;font-weight:700;color:#333}
.foot-p{font-size:12px;line-height:20px;color:#666}
.social{display:flex;gap:10px}
.social span{width:26px;height:26px;border:1px solid #bbb;display:block}
.contact-row{display:flex;gap:10px;align-items:flex-start;font-size:12px;line-height:18px;color:#555;margin-bottom:12px}
.badge{width:210px;height:88px;background:#fff;border:1px solid #ddd}
.badge span{display:block;margin:18px auto;width:170px;height:50px;background:#c8c8c8}
.copyright{left:0;top:3632px;width:1200px;height:49px;background:#e4e4e4;text-align:center;line-height:49px;font-size:12px;color:#666}
</style>
</head>
<body>

<header class="abs site-header">
  <div class="abs topbar">
    <span><i><svg width="14" height="14" viewBox="0 0 24 24"><path d="M6 2l4 4-2 3c1 3 4 6 7 7l3-2 4 4-3 4C10 22 2 14 2 5z" fill="var(--purple)"/></svg></i>+90 212 555 0147</span>
    <span><i><svg width="14" height="14" viewBox="0 0 24 24"><rect x="2" y="5" width="20" height="14" fill="var(--purple)"/><path d="M2 5l10 8 10-8" stroke="#fff" stroke-width="2" fill="none"/></svg></i>hello@klvrota.com</span>
  </div>
  <nav class="abs main-nav">
    <span class="active">Home</span><span>What We Do</span><span>Best Turkey Destinations ▾</span><span>KLV Team</span><span>Testimonials</span><span>Destino Turquia</span><span>Contact Us</span>
  </nav>
</header>
<div class="abs brand">KLV</div>
<div class="abs brand-line">Kestrel Lumen Voyages</div>

<section class="abs hero" role="img" aria-label="Close-up of blue evil-eye glass charms hanging from a tree branch"></section>
<h1 class="abs hero-title">OLD WORLD MYSTIQUE.&nbsp; NEW WORLD INNOVATION.<br>OUT-OF-THIS-WORLD SERVICE.</h1>
<div class="abs btn hero-btn">BOOK NOW !</div>
<div class="abs arrow-btn" style="left:26px;top:306px"><svg width="14" height="14" viewBox="0 0 14 14"><path d="M10 1L4 7l6 6" stroke="#fff" stroke-width="2.5" fill="none"/></svg></div>
<div class="abs arrow-btn" style="left:1124px;top:306px"><svg width="14" height="14" viewBox="0 0 14 14"><path d="M4 1l6 6-6 6" stroke="#fff" stroke-width="2.5" fill="none"/></svg></div>

<h2 class="abs sec-title" style="top:618px"><span class="mark"></span>WHAT WE DO BEST</h2>
<p class="abs intro">KLV has provided personalised and professional DMC service to all sectors of the corporate travel and meetings industry for almost 20 years. We've earned our excellent reputation by organising a multitude of successful and prestigious incentive programmes, executive meetings, conferences and events throughout TURKEY.</p>
<div class="abs services">
  <div class="service"><svg width="48" height="40" viewBox="0 0 48 40" fill="none" stroke="var(--purple)" stroke-width="3"><rect x="4" y="6" width="40" height="28"/><path d="M4 18h40M20 6v28"/></svg>Incentive Travel</div>
  <div class="service"><svg width="48" height="40" viewBox="0 0 48 40" fill="var(--purple)"><circle cx="24" cy="10" r="6"/><circle cx="10" cy="18" r="5"/><circle cx="38" cy="18" r="5"/><rect x="4" y="28" width="40" height="8"/></svg>Conferences<br>&amp; Meeting</div>
  <div class="service"><svg width="48" height="40" viewBox="0 0 48 40" fill="var(--purple)"><rect x="6" y="14" width="36" height="24"/><rect x="2" y="6" width="44" height="10"/></svg>Event Management &amp;<br>Product Launches</div>
  <div class="service"><svg width="48" height="40" viewBox="0 0 48 40" fill="none" stroke="var(--purple)" stroke-width="3"><path d="M24 3l6 13 14 1-11 9 4 14-13-8-13 8 4-14L4 17l14-1z"/></svg>VIP Travel</div>
  <div class="service"><svg width="48" height="40" viewBox="0 0 48 40" fill="none" stroke="var(--purple)" stroke-width="3"><circle cx="19" cy="24" r="11"/><circle cx="29" cy="18" r="11"/></svg>Destination<br>Weddings</div>
  <div class="service"><svg width="48" height="40" viewBox="0 0 48 40" fill="var(--purple)"><circle cx="10" cy="8" r="4"/><circle cx="24" cy="8" r="4"/><circle cx="38" cy="8" r="4"/><rect x="6" y="14" width="8" height="24"/><rect x="20" y="14" width="8" height="24"/><rect x="34" y="14" width="8" height="24"/></svg>Group Travel</div>
</div>

<div class="abs dest-panel" role="img" aria-label="Dim background photo of a historic mosque interior"></div>
<div class="abs dest-photo" role="img" aria-label="Blue Mosque with minarets under a clear blue sky"></div>
<h2 class="abs dest-title"><span class="mark"></span>OUR DESTINATIONS IN TURKEY</h2>
<p class="abs dest-text">KLV Designs And Operates Incentive Programmes, Meetings, Events In The Most Exciting Cities And Regions Of Turkey.</p>
<ul class="abs dest-list">
  <li class="on">ISTANBUL</li><li>CAPPADOCIA</li><li>BODRUM</li><li>NORTHERN CYPRUS</li><li>ANTALYA</li><li>IZMIR</li>
</ul>
<div class="abs btn dest-btn">VIEW ALL PLACES</div>
<div class="abs small-arrows">
  <span><svg width="10" height="10" viewBox="0 0 10 10"><path d="M7 1L3 5l4 4" stroke="#fff" stroke-width="2" fill="none"/></svg></span>
  <span><svg width="10" height="10" viewBox="0 0 10 10"><path d="M3 1l4 4-4 4" stroke="#fff" stroke-width="2" fill="none"/></svg></span>
</div>

<h2 class="abs sec-title" style="top:1605px"><span class="mark"></span>ANTALYA &amp; THE TURKISH RIVIERA</h2>
<article class="abs card" style="left:98px;top:1674px">
  <div class="card-photo" role="img" aria-label="Wooden gulet sailing boat moored in a harbour" style="background:linear-gradient(180deg,#8fb8dd,#5d7f9a 55%,#2c3f4f)"></div>
  <div class="card-shade"></div><h3>FOR INCENTIVES &amp; MEETINGS</h3>
  <p>Few coastlines in the world can offer anything close to ANTALYA's range of natural beauty, history, sport and culture.</p><span class="stars">★★★☆☆</span>
</article>
<article class="abs card" style="left:613px;top:1674px">
  <div class="card-photo" role="img" aria-label="Zip-line ride over a green river canyon" style="background:linear-gradient(180deg,#6f8f5a,#4f6b3e 50%,#3d5a5c)"></div>
  <div class="card-shade"></div><h3>FOR INCENTIVES &amp; MEETINGS</h3>
  <p>Few coastlines in the world can offer anything close to ANTALYA's range of natural beauty, history, sport and culture.</p><span class="stars">★★★☆☆</span>
</article>
<article class="abs card" style="left:98px;top:1995px">
  <div class="card-photo" role="img" aria-label="White travertine terraces with trees on the ridge" style="background:linear-gradient(180deg,#7aa3cf,#b9cde2 45%,#e6eef5 80%,#9fb8cc)"></div>
  <div class="card-shade"></div><h3>FOR INCENTIVES &amp; MEETINGS</h3>
  <p>Few coastlines in the world can offer anything close to ANTALYA's range of natural beauty, history, sport and culture.</p><span class="stars">★★★☆☆</span>
</article>
<article class="abs card" style="left:613px;top:1995px">
  <div class="card-photo" role="img" aria-label="Dinner table set on the deck of a yacht" style="background:linear-gradient(180deg,#d4d8dc,#8d9299 50%,#3c3f44)"></div>
  <div class="card-shade"></div><h3>FOR INCENTIVES &amp; MEETINGS</h3>
  <p>Few coastlines in the world can offer anything close to ANTALYA's range of natural beauty, history, sport and culture.</p><span class="stars">★★★☆☆</span>
</article>
<div class="abs btn view-btn">VIEW ALL</div>

<section class="abs join" role="img" aria-label="Warm dark background photo of an Ottoman interior"></section>
<div class="abs join-photo" role="img" aria-label="Photo of a company representative welcoming guests"></div>
<h2 class="abs join-title"><span class="mark"></span>JOIN US TODAY</h2>
<p class="abs join-text">We take pride in watching guests delight in unique country and culture-related features.</p>
<div class="abs join-input">Enter Your Email</div>
<div class="abs btn join-btn">SUBMIT</div>

<h2 class="abs sec-title" style="top:2866px"><span class="mark"></span>OUR BLOG</h2>
<div class="abs side-arrow" style="left:28px;top:3076px"><svg width="12" height="12" viewBox="0 0 12 12"><path d="M8 1L3 6l5 5" stroke="#888" stroke-width="2" fill="none"/></svg></div>
<div class="abs side-arrow" style="left:1128px;top:3076px"><svg width="12" height="12" viewBox="0 0 12 12"><path d="M4 1l5 5-5 5" stroke="#888" stroke-width="2" fill="none"/></svg></div>

<article class="abs post" style="left:98px;top:2937px">
  <div class="post-photo" role="img" aria-label="Candle-lit gala dinner tables" style="background:linear-gradient(180deg,#5a2a14,#a9582a 50%,#3a1a0e)"></div>
  <div class="post-date">AUG<br>25</div>
  <div class="post-meta">
    <span><svg width="11" height="11" viewBox="0 0 12 12"><circle cx="6" cy="3.5" r="3" fill="#444"/><path d="M0 12a6 5 0 0 1 12 0z" fill="#444"/></svg>Deniz</span>
    <span><svg width="12" height="11" viewBox="0 0 12 11"><path d="M1 1h10v7H5l-3 2V8H1z" fill="none" stroke="#444" stroke-width="1.3"/></svg>250</span>
    <span><svg width="12" height="11" viewBox="0 0 12 11"><path d="M6 10L1.5 5.5a2.6 2.6 0 0 1 4.5-3 2.6 2.6 0 0 1 4.5 3z" fill="none" stroke="#444" stroke-width="1.3"/></svg>34</span>
  </div>
  <h4>INCENTIVES &amp; CONVENTIONS</h4><p>With beautiful long, sandy beaches, charming mountain and fishing villages.</p><span class="more">READ MORE ➞</span>
</article>
<article class="abs post" style="left:447px;top:2937px">
  <div class="post-photo" role="img" aria-label="Whitewashed street with blue shutters and flowers" style="background:linear-gradient(90deg,#e9ecef,#9fc1de 50%,#d8dde2)"></div>
  <div class="post-date">AUG<br>25</div>
  <div class="post-meta">
    <span><svg width="11" height="11" viewBox="0 0 12 12"><circle cx="6" cy="3.5" r="3" fill="#444"/><path d="M0 12a6 5 0 0 1 12 0z" fill="#444"/></svg>Deniz</span>
    <span><svg width="12" height="11" viewBox="0 0 12 11"><path d="M1 1h10v7H5l-3 2V8H1z" fill="none" stroke="#444" stroke-width="1.3"/></svg>250</span>
    <span><svg width="12" height="11" viewBox="0 0 12 11"><path d="M6 10L1.5 5.5a2.6 2.6 0 0 1 4.5-3 2.6 2.6 0 0 1 4.5 3z" fill="none" stroke="#444" stroke-width="1.3"/></svg>34</span>
  </div>
  <h4>INCENTIVES &amp; CONVENTIONS</h4><p>With beautiful long, sandy beaches, charming mountain and fishing villages.</p><span class="more">READ MORE ➞</span>
</article>
<article class="abs post" style="left:795px;top:2937px">
  <div class="post-photo" role="img" aria-label="Colourful painted ceramic plates at a bazaar" style="background:linear-gradient(135deg,#c0392b,#2e6fa8 40%,#d4a21f 70%,#7b2d5e)"></div>
  <div class="post-date">AUG<br>25</div>
  <div class="post-meta">
    <span><svg width="11" height="11" viewBox="0 0 12 12"><circle cx="6" cy="3.5" r="3" fill="#444"/><path d="M0 12a6 5 0 0 1 12 0z" fill="#444"/></svg>Deniz</span>
    <span><svg width="12" height="11" viewBox="0 0 12 11"><path d="M1 1h10v7H5l-3 2V8H1z" fill="none" stroke="#444" stroke-width="1.3"/></svg>250</span>
    <span><svg width="12" height="11" viewBox="0 0 12 11"><path d="M6 10L1.5 5.5a2.6 2.6 0 0 1 4.5-3 2.6 2.6 0 0 1 4.5 3z" fill="none" stroke="#444" stroke-width="1.3"/></svg>34</span>
  </div>
  <h4>INCENTIVES &amp; CONVENTIONS</h4><p>With beautiful long, sandy beaches, charming mountain and fishing villages.</p><span class="more">READ MORE ➞</span>
</article>

<footer class="abs site-footer">
  <div class="abs" style="left:98px;top:48px;width:330px">
    <div class="foot-h">ABOUT US</div>
    <p class="foot-p" style="margin-top:18px">We are continually exploring all parts of the country in order to present the most thrilling options.</p>
    <p class="foot-p" style="margin-top:10px">We take pride in watching guests delight in unique countryand culture-related features.</p>
    <div class="social" style="margin-top:18px"><span></span><span></span><span></span><span></span></div>
  </div>
  <div class="abs" style="left:515px;top:48px;width:330px">
    <div class="foot-h" style="margin-bottom:18px">CONTACT US</div>
    <div class="contact-row"><svg width="10" height="14" viewBox="0 0 10 14"><path d="M5 0a5 5 0 0 1 5 5c0 4-5 9-5 9S0 9 0 5a5 5 0 0 1 5-5z" fill="var(--purple)"/><circle cx="5" cy="5" r="2" fill="#fff"/></svg><span>KLV – Kestrel Lumen Voyages<br>Lale Mah, Meltem Sok 12,<br>K2, D4, Karakoy<br>34420, Istanbul, TURKEY</span></div>
    <div class="contact-row"><svg width="12" height="12" viewBox="0 0 24 24"><path d="M6 2l4 4-2 3c1 3 4 6 7 7l3-2 4 4-3 4C10 22 2 14 2 5z" fill="var(--purple)"/></svg><span>+90 (0) 212 – 555 01 47</span></div>
    <div class="contact-row"><svg width="12" height="12" viewBox="0 0 12 12"><rect width="12" height="12" fill="var(--purple)"/></svg><span>+90 (0) 212 – 555 01 48</span></div>
    <div class="contact-row"><svg width="12" height="12" viewBox="0 0 24 24"><rect x="2" y="5" width="20" height="14" fill="var(--purple)"/></svg><span>www.klvrota.com</span></div>
  </div>
  <div class="abs badge" style="left:892px;top:34px"><span></span></div>
  <div class="abs badge" style="left:892px;top:144px"><span></span></div>
</footer>
<div class="abs copyright">Copyright © 2017, KLV. All Rights Reserved.</div>

</body>
</html>
```